Asia based real estate financing firm needs and AWESOME design for a biz card -Harbor Lending Circle

Looking for a stylish, & corporate-looking business card for a real estate financing brokerage firm in Asia, offering global mortgage loans. I uploaded our current logos. We would like to add a splash of color (perhaps the house icon) or any other suggestions are open. For the winning designer, we have a lot of work! Thanks and best of luck!

Target Market(s)

Real estate investors globally. We want to look more like a BANK and NOT a real estate company. Please don't play up on a "house" design.

Industry/Entity Type

Banking

Contact Information for Business Card

Harbor Lending Circle
Peter Wilks
Co-Founder | Partner

14 Cassia Lane, Suite 310
Singapore 047219
www.hlc-example.asia
peterwilks@hlc-example.asia
+65 555-0142
WeChat: peterwilks

Colors

Designer to choose colors to be used in the design.

Requirements
Must have
• Must have the standard business requirements for a card; name, address, email, etc
• Can be horizontal or vertical.
Nice to have
• It would be great to see some sort of variation to the logo with a pop of color. Red is good as we're in Asia, however, other options work as well.
• Our tag line is - Borderless mortgages. It doesn't have to be on the card but might be nice.
• I'd like to start seeing our tagline within the cards as well. - Borderless mortgages.
• Also, please add our location. The location for this card is Singapore so perhaps it can be highlighted or emphasised in some way.
• Singapore | Hong Kong | Shanghai | Manila
• As we will soon open an office in Shanghai, having an option for both languages would be great.
Should not have
• I'm exceited and open to your creativity ... knock it out of the park!

```html
<!DOCTYPE html>
<html lang="en">
<head>
<meta charset="utf-8">
<title>Harbor Lending Circle – Business Card</title>
<link rel="stylesheet" href="https://fonts.googleapis.com/css2?family=Open+Sans:ital,wght@1,400&family=Roboto+Condensed:ital,wght@1,500&family=Source+Sans+3:wght@600;700&display=swap">
<style>
  :root {
    --card-black: #0b0b0b;
    --accent-orange: #e8832f;
    --photo-light: #f0a35e;
    --photo-dark: #b85f1c;
    --ink-white: #ffffff;
    --page-white: #ffffff;
    --label-ink: #111111;
  }
  html, body {
    margin: 0;
    padding: 0;
    width: 1200px;
    height: 1200px;
    overflow: hidden;
    background: var(--page-white);
  }
  .canvas {
    position: relative;
    width: 1200px;
    height: 1200px;
  }
  .side-label {
    position: absolute;
    font-family: "Open Sans", sans-serif;
    font-style: italic;
    font-weight: 400;
    font-size: 74px;
    color: var(--label-ink);
    margin: 0;
    line-height: 1;
  }
  .side-label--front { left: 966px; top: 216px; }
  .side-label--back  { left: 40px;  top: 893px; }

  .card {
    position: absolute;
    width: 930px;
    height: 567px;
    background: var(--card-black);
    overflow: hidden;
    font-family: "Source Sans 3", sans-serif;
    color: var(--ink-white);
  }
  .card--front { left: 0; top: 0; }
  .card--back  { left: 270px; top: 633px; }

  .card__art {
    position: absolute;
    inset: 0;
    width: 100%;
    height: 100%;
  }

  /* Front */
  .holder-name {
    position: absolute;
    right: 638px;
    top: 170px;
    margin: 0;
    text-align: right;
    font-weight: 700;
    font-size: 66px;
    line-height: 56px;
    font-variant: small-caps;
    letter-spacing: -1px;
  }
  .divider {
    position: absolute;
    left: 312px;
    top: 108px;
    width: 3px;
    height: 248px;
    background: var(--ink-white);
  }
  .address {
    position: absolute;
    left: 327px;
    top: 122px;
    margin: 0;
    font-style: normal;
    font-weight: 700;
    font-size: 60px;
    line-height: 54px;
    letter-spacing: -0.5px;
  }
  .role {
    position: absolute;
    left: 108px;
    top: 416px;
    margin: 0;
    font-weight: 700;
    font-size: 36px;
  }
  .phone {
    position: absolute;
    left: 498px;
    top: 420px;
    display: flex;
    align-items: center;
    gap: 6px;
    font-weight: 700;
    font-size: 29px;
  }
  .phone svg { width: 24px; height: 42px; }
  .contact-line {
    position: absolute;
    top: 490px;
    margin: 0;
    font-weight: 700;
    font-size: 20px;
  }
  .contact-line--email  { left: 70px; }
  .contact-line--wechat { left: 410px; }

  /* Back */
  .brand-name {
    position: absolute;
    left: 0;
    width: 930px;
    top: 190px;
    margin: 0;
    text-align: center;
    font-weight: 600;
    font-size: 58px;
    letter-spacing: 1px;
    padding-left: 0;
  }
  .brand-name span { display: inline-block; transform: translateX(12px); }
  .offices {
    position: absolute;
    left: 118px;
    width: 700px;
    top: 340px;
    margin: 0;
    text-align: center;
    font-weight: 700;
    font-size: 37px;
    white-space: nowrap;
  }
  .tagline {
    position: absolute;
    left: 118px;
    width: 700px;
    top: 428px;
    margin: 0;
    text-align: center;
    font-family: "Roboto Condensed", sans-serif;
    font-style: italic;
    font-weight: 500;
    font-size: 35px;
  }
</style>
</head>
<body>
<main class="canvas">

  <section class="card card--front" aria-label="Business card front">
    <svg class="card__art" viewBox="0 0 930 567" aria-hidden="false">
      <defs>
        <linearGradient id="front-photo-tone" x1="0" y1="0" x2="1" y2="1">
          <stop offset="0" stop-color="var(--photo-light)"/>
          <stop offset="1" stop-color="var(--photo-dark)"/>
        </linearGradient>
      </defs>
      <polygon points="645,567 930,8 930,256 774,567" fill="var(--accent-orange)"/>
      <polygon role="img" aria-label="Photo of the Merlion statue tinted orange"
               points="712,430 800,200 930,190 930,256 774,567 700,567"
               fill="url(#front-photo-tone)" opacity="0.55"/>
    </svg>

    <h1 class="holder-name">Peter<br>Wilks</h1>
    <div class="divider"></div>
    <address class="address">14 Cassia<br>Lane, Suite 310<br>Singapore<br>047219</address>

    <p class="role">Co-Founder | Partner</p>
    <div class="phone">
      <svg viewBox="0 0 24 42" aria-hidden="true">
        <path d="M7 3 C3 5 2 10 3 18 C4 27 8 34 14 39 L18 36 C19 35 19 34 18 33 L14 28 C13 27 12 27 11 28 L10 29 C8 25 7 20 7 15 L9 14 C10 13 10 12 10 11 L9 4 C9 3 8 2 7 3 Z" fill="var(--ink-white)"/>
      </svg>
      <span>+65 555-0142</span>
    </div>
    <p class="contact-line contact-line--email">@: peterwilks@hlc-example.asia</p>
    <p class="contact-line contact-line--wechat">WeChat: peterwilks</p>
  </section>

  <h2 class="side-label side-label--front">FRONT</h2>

  <section class="card card--back" aria-label="Business card back">
    <svg class="card__art" viewBox="0 0 930 567">
      <defs>
        <linearGradient id="back-photo-tone" x1="0" y1="0" x2="1" y2="1">
          <stop offset="0" stop-color="var(--photo-light)"/>
          <stop offset="1" stop-color="var(--photo-dark)"/>
        </linearGradient>
      </defs>
      <polygon points="0,0 32,0 286,567 150,567 0,300" fill="var(--accent-orange)"/>
      <polygon role="img" aria-label="Photo of the Merlion statue tinted orange"
               points="0,220 140,210 190,360 200,567 150,567 0,300"
               fill="url(#back-photo-tone)" opacity="0.55"/>
    </svg>

    <p class="brand-name"><span>Harbor Lending Circle</span></p>
    <p class="offices">Singapore | Hong Kong | Shanghai | Manila</p>
    <p class="tagline">“Borderless Mortgages”</p>
  </section>

  <h2 class="side-label side-label--back">BACK</h2>

</main>
</body>
</html>
```